Med Spa business card design with logo

Need a logo design and business card for our new company Velora Skinworks Med Spa. We are a medical office that deals with high end clients. We offer them skin care products which include NERVAX, lip augmentation, and various laser for the skin. I king of like the logo attached, maybe something along those lines but also open to any logo concept.
Updates

Target Market(s)

Out target audience are male and females in the age range of 21-80 years of age

Industry/Entity Type

Medical

Contact Information for Business Card

woukd like front of card to have logo and business name VELORA SKINWORKS MEDSPA. Back of card employee name and phone number along with instagram logo and user name

Font styles to use
Serif
Sans Serif

Requirements
Must have
• prefer monochromatic look white, black, gold
Should not have
• not too colorful

```html
<!DOCTYPE html>
<html lang="en">
<head>
<meta charset="UTF-8">
<title>Velora Skinworks Med Spa – Business Card</title>
<link rel="stylesheet" href="https://fonts.googleapis.com/css2?family=Cinzel:wght@400;500&family=Source+Sans+3:wght@400;600&display=swap">
<style>
  :root {
    --backdrop: #000000;
    --card: #2f3034;
    --card-edge: #3a3b40;
    --gold: #f3ae1f;
    --gold-soft: #f7c34a;
    --white: #f2f2f2;
    --rose-line: #b2495b;
    --medspa: #c9c2c4;
    --divider: #45464b;
  }
  * { margin: 0; padding: 0; box-sizing: border-box; }
  html, body {
    width: 1200px; height: 900px; overflow: hidden;
    background: var(--backdrop);
  }
  .canvas { position: relative; width: 1200px; height: 900px; }
  .card {
    position: absolute; top: 271px; width: 457px; height: 281px;
    background: var(--card); border-radius: 14px;
    box-shadow: inset 0 0 0 1px var(--card-edge);
  }
  .card--contact { left: 137px; }
  .card--brand { left: 626px; }

  .monogram-name {
    position: absolute; left: 50px; top: 104px; width: 170px;
    font-family: "Cinzel", serif; font-weight: 500; font-size: 21px;
    line-height: 1.25; color: var(--gold); text-align: center;
  }
  .divider {
    position: absolute; left: 230px; top: 80px; width: 1px; height: 115px;
    background: var(--divider);
  }
  .person { position: absolute; left: 258px; top: 80px; font-family: "Source Sans 3", sans-serif; }
  .person__name { font-weight: 600; font-size: 17px; color: var(--gold); line-height: 22px; }
  .person__title { font-size: 13px; color: var(--white); line-height: 18px; }
  .contacts {
    position: absolute; left: 258px; top: 144px; list-style: none;
    font-family: "Source Sans 3", sans-serif; font-size: 13px; color: var(--white);
  }
  .contacts li { display: flex; align-items: center; height: 19px; }
  .contacts svg { width: 10px; height: 10px; margin-right: 9px; flex: none; }

  .brand-circle {
    position: absolute; left: 205px; top: 80px; width: 46px; height: 46px;
    border: 2px solid var(--gold); border-radius: 50%;
  }
  .wordmark {
    position: absolute; left: 0; right: 0; top: 156px; text-align: center;
    font-family: "Cinzel", serif; font-weight: 400; font-size: 24px;
    letter-spacing: 0.5px; color: var(--gold);
  }
  .wordmark__rule {
    position: absolute; left: 91px; width: 275px; top: 193px; height: 1px;
    background: var(--rose-line);
  }
  .wordmark__sub {
    position: absolute; left: 0; right: 0; top: 186px; text-align: center;
  }
  .wordmark__sub span {
    background: var(--card); padding: 0 6px;
    font-family: "Cinzel", serif; font-size: 11px; letter-spacing: 2.5px; color: var(--medspa);
  }
</style>
</head>
<body>
<main class="canvas">
  <section class="card card--contact">
    <div class="monogram-name">Velora Skinworks Med Spa</div>
    <div class="divider"></div>
    <div class="person">
      <p class="person__name">Adrian Hale</p>
      <p class="person__title">Managing Director</p>
    </div>
    <ul class="contacts">
      <li>
        <svg viewBox="0 0 10 10"><path fill="#f3ae1f" d="M2 0.5 L3.6 2.6 L2.8 3.6 Q4 6 6.4 7.2 L7.4 6.4 L9.5 8 L8.5 9.5 Q2 9 0.5 1.5 Z"/></svg>
        (044)-318-2675
      </li>
      <li>
        <svg viewBox="0 0 10 10"><rect x="0.5" y="2" width="9" height="6.5" fill="#f3ae1f"/><path d="M0.8 2.3 L5 5.6 L9.2 2.3" fill="none" stroke="#2f3034" stroke-width="0.9"/></svg>
        hello@veloraskin.com
      </li>
      <li>
        <svg viewBox="0 0 10 10"><rect x="0.5" y="0.5" width="9" height="9" rx="1.5" fill="#f3ae1f"/></svg>
        veloraskinworksmedspa
      </li>
    </ul>
  </section>

  <section class="card card--brand">
    <div class="brand-circle"></div>
    <h1 class="wordmark">VELORA SKINWORKS</h1>
    <div class="wordmark__rule"></div>
    <p class="wordmark__sub"><span>MEDSPA</span></p>
  </section>
</main>
</body>
</html>
```